4" x 6" Coffee Label for a Fundraising Project

You will be designing a full-color label for a coffee product.
This particular design is for a school band fundraising program, and should align with the school existing webiste in terms of 'look and feel.'
You may choose any one of the following coffee blends to build your design around: breakfast blend, sumatra, hazelnut, house blend decaf, mocha, pumpkin spice, candy cane or cinnabun. (Yes, we will need multiple labels in the near future.) Your design for a label should be expandable to other coffee varieties and leverage some brand elements across different labels to reflect brand consistency.
What is the brand? It is a k-12 school, the fundraisor is for the school's music / band program. The primary colors are red, white and black; however you should incorporate other colors that represent the coffee blend (from the above list).
Who is the target market? Coffee drinkers! (So your design should reflect the positive qualities of coffee) They are also parents, friends and alumni of the school.
What is the brand's feel? Your design should bring to mind the following when drinkers view the label on the package: high quality, a luxury drink, aligned with christian values, perhaps a sense of community, and the school's band and/or performing arts. (Please note that this design is specific to the band program.)
Can I create a name for any of the above blends that has band connetations? Yes! Actually, ideating band-related names is encouraged. If your design uses Lantern Meadow or Copper Ballad for the breakfast blend, or Tawny Tango or Velvet Fanfare for the mocha blend - AWESOME! So get creative in renaming the blends appropraitely and incorporating this into your overall design. Even better if your naming convention and design could be leveraged across several different coffee blends.
If you incorporate photo imagery in your design, note that we will need to procure similar images we own or can license. Thus, photo imagery should be FPO and representative of they type of imagery for the design.
Specifications for the design are:
1. 4" wide x 6" tall portrait layout
2. 1600 x 2400 pixes
3. CYML for printing
4. Note that the bottom third must be left completely clean - no design elements or text - for NQB required labeling.
5. Design must be completed in Adobe Photoshop or Illustrator.
6. All incorporated fonts must be available for use without licensing.

```html
<!DOCTYPE html>
<html lang="en">
<head>
<meta charset="utf-8">
<title>Copper Ballad – Breakfast Blend Label</title>
<link rel="stylesheet" href="https://fonts.googleapis.com/css2?family=Lobster&family=Raleway:wght@500;600&display=swap">
<style>
  :root {
    --backdrop: #666666;
    --label-black: #000000;
    --brand-red: #ff0000;
    --white: #ffffff;
    --leaf-green: #3f7a4e;
    --leaf-dark: #24472f;
    --sketch-grey: #2e2e2e;
    --sketch-light: #4a4a4a;
  }
  * { box-sizing: border-box; margin: 0; padding: 0; }
  html, body {
    width: 848px; height: 1200px; overflow: hidden;
    background: var(--backdrop);
  }
  .label {
    position: absolute; left: 82px; top: 87px;
    width: 684px; height: 1026px;
    background: var(--white);
    box-shadow: 0 6px 16px rgba(0,0,0,0.45);
    overflow: hidden;
  }
  .label__artwork {
    position: absolute; left: 0; top: 0; width: 684px; height: 680px;
    background: var(--label-black);
  }

  /* Illustration areas */
  .foliage {
    position: absolute; top: 0; height: 170px;
    background: linear-gradient(to bottom, var(--leaf-green) 0%, var(--leaf-dark) 70%, var(--label-black) 100%);
  }
  .foliage--left { left: 0; width: 245px; }
  .foliage--right { left: 437px; width: 247px; }
  .saxophone {
    position: absolute; left: 470px; top: 228px; width: 180px; height: 190px;
    border-radius: 10px;
    background: linear-gradient(160deg, var(--sketch-light) 0%, var(--sketch-grey) 100%);
  }

  /* Brand block */
  .brand-block {
    position: absolute; left: 245px; top: 0; width: 192px; height: 160px;
    background: var(--brand-red);
    display: flex; flex-direction: column; align-items: center; justify-content: center;
    gap: 10px;
  }
  .brand-block__dot {
    width: 66px; height: 66px; border-radius: 50%; background: var(--white);
  }
  .brand-block__name {
    font-family: 'Raleway', sans-serif; font-weight: 600;
    font-size: 22px; color: var(--white); letter-spacing: 1px;
  }
  .category {
    position: absolute; left: 0; top: 168px; width: 684px;
    text-align: center;
    font-family: 'Raleway', sans-serif; font-weight: 500;
    font-size: 30px; line-height: 1; letter-spacing: 11px; padding-left: 11px;
    color: var(--white);
  }

  /* Blend name */
  .blend-name {
    position: absolute; left: 70px; top: 212px; width: 420px;
    font-family: 'Lobster', cursive; font-weight: 400; color: var(--white);
    text-shadow: 0 0 10px rgba(255,255,255,0.45), 2px 3px 4px rgba(0,0,0,0.8);
    line-height: 0.92;
  }
  .blend-name__line { display: block; font-size: 96px; }
  .blend-name__line--second { padding-left: 95px; }

  /* Ribbon and seal */
  .ribbon {
    position: absolute; left: 0; top: 478px; width: 684px; height: 100px;
    background: var(--brand-red);
  }
  .ribbon__rule {
    position: absolute; left: 0; width: 684px; height: 2px; background: var(--white);
  }
  .ribbon__rule--top { top: 12px; }
  .ribbon__rule--bottom { top: 86px; }
  .ribbon__word {
    position: absolute; top: 0; width: 215px; height: 100px;
    display: flex; align-items: center; justify-content: center;
    font-family: 'Lobster', cursive; font-size: 42px; color: var(--label-black);
  }
  .ribbon__word--left { left: 0; }
  .ribbon__word--right { left: 469px; }
  .seal {
    position: absolute; left: 217px; top: 403px; width: 250px; height: 250px;
    filter: drop-shadow(0 0 8px rgba(0,0,0,0.45));
  }

  /* Supporting copy */
  .tagline {
    position: absolute; left: 0; top: 604px; width: 215px;
    text-align: center;
    font-family: 'Lobster', cursive; font-size: 22px; line-height: 1.2;
    color: var(--white);
  }
  .net-weight {
    position: absolute; left: 469px; top: 606px; width: 215px;
    text-align: center;
    font-family: 'Raleway', sans-serif; font-weight: 500;
    font-size: 19px; line-height: 1.25; color: var(--white);
  }
  .net-weight__amount { font-weight: 600; font-size: 24px; }

  /* Clean zone reserved for required labeling */
  .regulatory-area {
    position: absolute; left: 0; top: 680px; width: 684px; height: 346px;
    background: var(--white);
  }
</style>
</head>
<body>
  <main class="label">
    <section class="label__artwork">
      <div class="foliage foliage--left" role="img" aria-label="Illustrated coffee branches with leaves, white blossoms and red cherries"></div>
      <div class="foliage foliage--right" role="img" aria-label="Illustrated coffee branches with leaves, white blossoms and red cherries"></div>

      <div class="brand-block">
        <span class="brand-block__dot"></span>
        <span class="brand-block__name">Crestview</span>
      </div>
      <p class="category">COFFEE</p>

      <div class="saxophone" role="img" aria-label="Line-drawn saxophone illustration"></div>

      <h1 class="blend-name">
        <span class="blend-name__line">Copper</span>
        <span class="blend-name__line blend-name__line--second">Ballad</span>
      </h1>

      <div class="ribbon">
        <span class="ribbon__rule ribbon__rule--top"></span>
        <span class="ribbon__rule ribbon__rule--bottom"></span>
        <span class="ribbon__word ribbon__word--left">Breakfast</span>
        <span class="ribbon__word ribbon__word--right">Blend</span>
      </div>

      <svg class="seal" viewBox="0 0 250 250" aria-hidden="true">
        <polygon points="125,15 162.5,34.4 202.8,47.2 215.6,87.5 235,125 215.6,162.5 202.8,202.8 162.5,215.6 125,235 87.5,215.6 47.2,202.8 34.4,162.5 15,125 34.4,87.5 47.2,47.2 87.5,34.4"
                 fill="var(--brand-red)" stroke="var(--brand-red)" stroke-width="20" stroke-linejoin="round"/>
        <circle cx="125" cy="125" r="96" fill="none" stroke="var(--white)" stroke-width="2.5"/>
        <g fill="none" stroke="var(--white)" stroke-width="4.5" stroke-linecap="round" stroke-linejoin="round">
          <path d="M80 128 H152 C153 160 136 176 116 176 C96 176 80 160 80 128 Z"/>
          <path d="M151 138 C168 134 175 150 160 160 L145 167"/>
          <path d="M108 110 C98 100 114 92 106 80"/>
          <path d="M122 112 C110 98 130 88 120 74 C115 67 124 62 122 57"/>
          <path d="M134 110 C126 100 140 92 134 82"/>
        </g>
      </svg>

      <p class="tagline">a bright, smooth<br>breakfast blend</p>
      <p class="net-weight"><span class="net-weight__amount">2</span> Lb. Whole<br>Bean Coffee</p>
    </section>
    <section class="regulatory-area"></section>
  </main>
</body>
</html>
```